Webdesign für Bilderbücher für Kinder
Zielgruppe
Wir sind ein Verlag für zweisprachige Bilderbücher für Kinder im Alter von 2-8 Jahren. Wir suchen ein Design für eine mit SHOPIFY neu zu erstellende Website, über die die Bücher verkauft werden sollen.
Der Verlag ist das deutsche Imprint eines internationalen Autoren (zur Orientierung siehe www.tarekvossbooks.com oder kurz.lk/tarekvoss).
Da das Thema sehr bunt ist und mit der Sprachen-Niche noch nicht prominent besetzt ist, wollen wir hier bewusst NICHT so viele Vorgaben machen, was das Design angeht.
Aufgabenstellung
Logo und Beispiele aus bestehenden Büchern sind als Attachments angehängt.
Beispielseiten zur Orientierung, die uns gefallen, sind die folgenden:
https://www.tarekvossbooks.com/
https://www.edition-lomatu.com/
Ein gutes Design hat der Wolkenkamm Verlag
https://www.wolkenkammverlag.de/
oder der Trivel Verlag
https://shop.trivel-verlag.de/

```html
<!DOCTYPE html>
<html lang="de">
<head>
<meta charset="utf-8">
<title>Sonnenfeld Verlag – Shop Entwurf</title>
<link href="https://fonts.googleapis.com/css2?family=Work+Sans:wght@400;500;600&family=Lora:wght@400;500&display=swap" rel="stylesheet">
<style>
:root{
  --stage:#cccccc;
  --paper:#ffffff;
  --sand:#e9e4de;
  --blue:#45697f;
  --ink:#3a3a3a;
  --muted:#7b7b7b;
  --accent:#c9484a;
  --shade:#6c6c6c;
}
*{box-sizing:border-box;margin:0;padding:0}
html,body{width:702px;height:1200px;overflow:hidden;background:var(--stage)}
body{position:relative;font-family:"Work Sans",sans-serif;color:var(--ink)}
h1,h2,h4{font-weight:400}
.page{position:absolute;background:var(--paper);overflow:hidden}
.page--home{left:97px;top:128px;width:257px;height:946px}
.page--product{left:367px;top:128px;width:257px;height:581px}
.abs{position:absolute}
.brand{font-family:"Lora",serif;font-size:4px;color:var(--blue);white-space:nowrap;display:flex;align-items:center;gap:1.5px}
.brand__dot{width:2.5px;height:2.5px;border-radius:50%;background:var(--accent)}
.nav a{position:absolute;font-size:3.2px;color:var(--muted);text-decoration:none;white-space:nowrap}
.nav a.is-active{color:var(--accent);border-bottom:.4px solid var(--accent)}
.icon{position:absolute;width:5px;height:5px}
.eyebrow{font-size:3px;color:var(--muted)}
.hero__title{font-size:9.2px;line-height:10.4px;font-weight:600;color:var(--blue);letter-spacing:.2px}
.hero__text{font-size:2.8px;line-height:5.8px;color:var(--muted)}
.img{position:absolute}
.shelf{position:absolute;left:0;width:257px;height:180px}
.shelf__title{position:absolute;left:19px;top:0;font-family:"Lora",serif;font-weight:400;font-size:4.6px;color:var(--ink);display:flex;align-items:center;gap:3px;width:218px}
.shelf__title::after{content:"";flex:1;height:.4px;background:#b9b9b9}
.tile{position:absolute;background:var(--sand);display:flex;align-items:center;justify-content:center}
.tile--feature{left:20px;top:13px;width:105px;height:132px;background:var(--shade);flex-direction:column;color:#fff;font-family:"Lora",serif;text-align:center}
.tile--feature .cover{position:absolute;left:17px;top:25px;width:72px;height:92px;opacity:.35}
.tile--feature .label{position:relative;font-size:4.4px;line-height:5px}
.tile--feature .price{position:relative;font-size:7.5px;margin-top:4px}
.cover{width:39px;height:38px;box-shadow:1px 1px 2px rgba(0,0,0,.25)}
.cover--frog{background:linear-gradient(180deg,#dbe9f2 0%,#f2efe2 55%,#b8d07a 100%)}
.cover--moon{background:linear-gradient(180deg,#8fbfdc 0%,#b8d59a 60%,#93b45c 100%)}
.arrow{position:absolute;width:16px;height:16px;border-radius:50%;background:#fff;box-shadow:0 0 3px rgba(0,0,0,.25);display:flex;align-items:center;justify-content:center}
.social{position:absolute;display:flex;gap:7px}
.social span{width:4.5px;height:4.5px;border-radius:50%;border:.6px solid var(--ink)}
.foot h4{font-size:3px;font-weight:600;color:var(--blue)}
.foot p,.foot li{font-size:2.8px;line-height:4.6px;color:var(--blue);list-style:none}
.copy{font-size:2.8px;color:var(--blue);text-align:center;width:100%}
.insta{position:absolute;left:0;top:669px;width:257px;height:124px;background:var(--sand)}
.insta__handle{position:absolute;left:19px;top:8px;font-size:4px;color:#fff;font-weight:500}
.news{position:absolute;left:36px;top:787px;width:185px;height:42px;background:#fff;box-shadow:0 1px 4px rgba(0,0,0,.15)}
.news__title{position:absolute;left:13px;top:9px;font-size:2.8px;font-weight:600;color:var(--blue)}
.news__field{position:absolute;left:13px;top:19px;width:50px;height:6px;border:.4px solid #ccc;font-size:2.4px;color:#bbb;padding-left:5px;line-height:5.6px}
.news__btn{position:absolute;left:69px;top:19px;width:22px;height:6px;background:var(--blue);color:#fff;font-size:2.6px;font-weight:600;text-align:center;line-height:6px}
.news__side{position:absolute;left:99px;top:0;width:86px;height:42px;background:var(--blue);color:#fff;text-align:center}
.news__side p{font-size:2.7px;line-height:3.8px;margin-top:9px}
.news__side .social{left:28px;top:21px}
.news__side .social span{border-color:#fff;width:6px;height:6px}
.crumb{font-size:3px;line-height:4.5px;color:var(--muted)}
.crumb b{font-weight:400;color:var(--blue)}
.gallery{position:absolute;left:18px;top:47px;width:113px;height:290px;background:var(--sand)}
.info{position:absolute;left:139px;width:100px;font-family:"Lora",serif}
.info__author{font-family:"Work Sans",sans-serif;font-size:3px;color:var(--blue)}
.info__title{font-size:6.2px;line-height:8.4px;color:var(--blue);letter-spacing:.2px;font-weight:400}
.info__price{font-size:5px;color:var(--blue)}
.info__small{font-size:2.7px;color:var(--muted);font-style:italic}
.qty{display:flex;align-items:center;gap:3px;font-size:2.7px;color:var(--muted);font-family:"Work Sans",sans-serif}
.qty span{border:.4px solid #ccc;padding:0 4px;line-height:4px}
.btn{position:absolute;left:0;width:75px;font-size:2.8px;text-align:center;font-family:"Lora",serif}
.btn--line{border:.4px solid #ddd;color:var(--muted);height:7px;line-height:7px}
.btn--solid{background:var(--blue);color:#fff;height:8px;line-height:8px}
.desc{font-family:"Work Sans",sans-serif;font-size:2.6px;line-height:4.1px;color:var(--blue)}
.desc p{margin-bottom:4.1px}
.specs dt{font-size:2.8px;font-weight:500;color:var(--blue);line-height:3.8px}
.specs dd{font-size:2.7px;color:var(--muted);line-height:3.8px;margin-bottom:3.3px}
.related__title{position:absolute;left:18px;top:369px;font-family:"Lora",serif;font-size:4.6px;color:var(--blue);font-weight:400}
.related__tile{position:absolute;top:381px;width:53px;height:66px;background:var(--sand);display:flex;align-items:center;justify-content:center}
.related__tile .cover{width:36px;height:36px}
.related__cap{position:absolute;top:452px;width:53px;font-family:"Lora",serif;font-size:2.7px;line-height:3.6px;color:var(--muted)}
</style>
</head>
<body>

<!-- Startseite -->
<section class="page page--home">
  <div class="brand abs" style="left:19px;top:18px"><span class="brand__dot"></span>Sonnenfeld verlag</div>
  <nav class="nav">
    <a class="is-active" style="left:126px;top:18px">Start</a>
    <a style="left:140px;top:18px">Bücher</a>
    <a style="left:158px;top:18px">Verlag</a>
    <a style="left:175px;top:18px">Kitas/Schulen</a>
    <a style="left:203px;top:18px">Blog</a>
  </nav>
  <svg class="icon" style="left:218px;top:17.5px" viewBox="0 0 10 10"><circle cx="4" cy="4" r="3" fill="none" stroke="#555" stroke-width="1"/><path d="M6.3 6.3 9 9" stroke="#555" stroke-width="1"/></svg>
  <svg class="icon" style="left:229px;top:17px" viewBox="0 0 10 10"><rect x="1.5" y="3" width="7" height="6" fill="none" stroke="#555" stroke-width=".9"/><path d="M3.5 3V2a1.5 1.5 0 0 1 3 0v1" fill="none" stroke="#555" stroke-width=".9"/></svg>

  <p class="eyebrow abs" style="left:19px;top:38.5px">Schön, dass du da bist!</p>
  <h1 class="hero__title abs" style="left:19px;top:51px;width:105px">Wir sind der Trivel Verlag. Wir lieben Bücher.</h1>
  <p class="hero__text abs" style="left:19px;top:87px;width:90px">Wir machen Bilderbücher für kleine Leser in zwei Sprachen. Jede Seite lädt zum Vorlesen, Staunen und gemeinsamen Lernen ein. Unsere Geschichten reisen von Haus zu Haus und wecken Freude an neuen Wörtern und Bildern für die ganze Familie.</p>
  <div class="img" role="img" aria-label="Foto: zwei Kinder lesen abends gemeinsam ein Buch im Licht einer Lampe" style="left:124px;top:34px;width:133px;height:107px;background:linear-gradient(160deg,#8fa7b7 0%,#5f7683 45%,#3c3f47 100%)"></div>

  <div class="shelf" style="top:157px">
    <h2 class="shelf__title">Bilingual Books</h2>
    <div class="tile tile--feature"><div class="cover cover--moon" role="img" aria-label="Buchcover Der tanzende Mond"></div><span class="label">Der tanzende Mond<br>The Dancing Moon</span><span class="price">$11,95</span></div>
    <div class="tile" style="left:129px;top:13px;width:52px;height:64px"><div class="cover cover--frog" role="img" aria-label="Buchcover Hüpf, kleiner Frosch"></div></div>
    <div class="tile" style="left:184px;top:13px;width:53px;height:64px"><div class="cover cover--moon" role="img" aria-label="Buchcover Der tanzende Mond"></div></div>
    <div class="tile" style="left:129px;top:81px;width:52px;height:64px"><div class="cover cover--frog" role="img" aria-label="Buchcover Hüpf, kleiner Frosch"></div></div>
    <div class="tile" style="left:184px;top:81px;width:53px;height:64px"><div class="cover cover--moon" role="img" aria-label="Buchcover Der tanzende Mond"></div></div>
    <div class="arrow" style="left:12px;top:68px"><svg width="6" height="6" viewBox="0 0 10 10"><path d="M6.5 1.5 3 5l3.5 3.5" fill="none" stroke="#444" stroke-width="1.3"/></svg></div>
    <div class="arrow" style="left:229px;top:68px"><svg width="6" height="6" viewBox="0 0 10 10"><path d="M3.5 1.5 7 5 3.5 8.5" fill="none" stroke="#444" stroke-width="1.3"/></svg></div>
  </div>

  <div class="shelf" style="top:328px">
    <h2 class="shelf__title">One Language Books</h2>
    <div class="tile tile--feature"><div class="cover cover--moon" role="img" aria-label="Buchcover Der tanzende Mond"></div><span class="label">Der tanzende Mond<br>The Dancing Moon</span><span class="price">$11,95</span></div>
    <div class="tile" style="left:129px;top:13px;width:52px;height:64px"><div class="cover cover--frog" role="img" aria-label="Buchcover Hüpf, kleiner Frosch"></div></div>
    <div class="tile" style="left:184px;top:13px;width:53px;height:64px"><div class="cover cover--moon" role="img" aria-label="Buchcover Der tanzende Mond"></div></div>
    <div class="tile" style="left:129px;top:81px;width:52px;height:64px"><div class="cover cover--frog" role="img" aria-label="Buchcover Hüpf, kleiner Frosch"></div></div>
    <div class="tile" style="left:184px;top:81px;width:53px;height:64px"><div class="cover cover--moon" role="img" aria-label="Buchcover Der tanzende Mond"></div></div>
    <div class="arrow" style="left:12px;top:68px"><svg width="6" height="6" viewBox="0 0 10 10"><path d="M6.5 1.5 3 5l3.5 3.5" fill="none" stroke="#444" stroke-width="1.3"/></svg></div>
    <div class="arrow" style="left:229px;top:68px"><svg width="6" height="6" viewBox="0 0 10 10"><path d="M3.5 1.5 7 5 3.5 8.5" fill="none" stroke="#444" stroke-width="1.3"/></svg></div>
  </div>

  <div class="shelf" style="top:500px">
    <h2 class="shelf__title">Activity Books</h2>
    <div class="tile tile--feature"><div class="cover cover--moon" role="img" aria-label="Buchcover Der tanzende Mond"></div><span class="label">Der tanzende Mond<br>The Dancing Moon</span><span class="price">$11,95</span></div>
    <div class="tile" style="left:129px;top:13px;width:52px;height:64px"><div class="cover cover--frog" role="img" aria-label="Buchcover Hüpf, kleiner Frosch"></div></div>
    <div class="tile" style="left:184px;top:13px;width:53px;height:64px"><div class="cover cover--moon" role="img" aria-label="Buchcover Der tanzende Mond"></div></div>
    <div class="tile" style="left:129px;top:81px;width:52px;height:64px"><div class="cover cover--frog" role="img" aria-label="Buchcover Hüpf, kleiner Frosch"></div></div>
    <div class="tile" style="left:184px;top:81px;width:53px;height:64px"><div class="cover cover--moon" role="img" aria-label="Buchcover Der tanzende Mond"></div></div>
    <div class="arrow" style="left:12px;top:68px"><svg width="6" height="6" viewBox="0 0 10 10"><path d="M6.5 1.5 3 5l3.5 3.5" fill="none" stroke="#444" stroke-width="1.3"/></svg></div>
    <div class="arrow" style="left:229px;top:68px"><svg width="6" height="6" viewBox="0 0 10 10"><path d="M3.5 1.5 7 5 3.5 8.5" fill="none" stroke="#444" stroke-width="1.3"/></svg></div>
  </div>

  <div class="insta">
    <span class="insta__handle">@tarekplanet</span>
    <div class="img" role="img" aria-label="Buchcover Keine Angst, Opa! mit einer Fahrradszene" style="left:19px;top:18px;width:86px;height:86px;background:linear-gradient(170deg,#f4e2a8 0%,#f0b45e 60%,#e08a3c 100%)"></div>
    <div class="img" role="img" aria-label="Foto: gemeinsames Vorlesen" style="left:108px;top:18px;width:42px;height:42px;background:linear-gradient(160deg,#f6e9e3,#d9b7a5)"></div>
    <div class="img" role="img" aria-label="Ausmalbild Schlafenszeit" style="left:153px;top:18px;width:42px;height:42px;background:linear-gradient(160deg,#f4efe6,#ddd7c8)"></div>
    <div class="img" role="img" aria-label="Buchcover Hüpf, kleiner Frosch" style="left:198px;top:18px;width:42px;height:42px;background:linear-gradient(180deg,#c9a878,#dbe9f2 30%,#b8d07a)"></div>
    <div class="img" role="img" aria-label="Buchcover Hüpf, kleiner Frosch" style="left:108px;top:63px;width:42px;height:41px;background:linear-gradient(180deg,#c9a878,#dbe9f2 30%,#b8d07a)"></div>
    <div class="img" role="img" aria-label="Ausmalbild Schlafenszeit" style="left:153px;top:63px;width:42px;height:41px;background:linear-gradient(160deg,#f4efe6,#ddd7c8)"></div>
    <div class="img" role="img" aria-label="Buchcover Keine Angst, Opa!" style="left:198px;top:63px;width:42px;height:41px;background:linear-gradient(170deg,#f4e2a8,#e08a3c)"></div>
  </div>

  <div class="news">
    <p class="news__title">GET SPECIAL OFFERS IN YOUR INBOX</p>
    <div class="news__field">example@mail.com</div>
    <div class="news__btn">SUBMIT</div>
    <div class="news__side"><p>Follow our social media accounts<br>for news and updates</p><div class="social"><span></span><span></span><span></span></div></div>
  </div>

  <footer class="foot">
    <div class="abs" style="left:20px;top:881px;width:90px"><h4>Kundenservice</h4><p style="margin-top:4px">Du hast Fragen zu unseren Büchern oder Deiner Bestellung?<br>Meld Dich einfach bei <b>hallo@sonnenfeldverlag.de</b> – wir antworten so schnell es geht.</p></div>
    <div class="abs" style="left:141px;top:881px"><h4>Kontakt</h4><ul style="margin-top:4px"><li>Handel</li><li>Presse</li><li>Karriere</li></ul></div>
    <div class="abs" style="left:195px;top:881px"><h4>Kleingedrucktes</h4><ul style="margin-top:4px"><li>Impressum</li><li>AGB</li><li>Datenschutzerklärung</li></ul></div>
    <div class="social" style="left:21px;top:921px"><span></span><span></span><span></span></div>
    <p class="copy abs" style="left:0;top:934px">© 2022, Sonnenfeld Verlag</p>
  </footer>
</section>

<!-- Produktseite -->
<section class="page page--product">
  <div class="brand abs" style="left:18px;top:19px"><span class="brand__dot"></span>Sonnenfeld verlag</div>
  <nav class="nav">
    <a class="is-active" style="left:55px;top:19px">Start</a>
    <a style="left:69px;top:19px">Bücher</a>
    <a style="left:87px;top:19px">Verlag</a>
    <a style="left:103px;top:19px">Kitas/Schulen</a>
    <a style="left:132px;top:19px">Blog</a>
  </nav>
  <svg class="icon" style="left:218px;top:17.5px" viewBox="0 0 10 10"><circle cx="4" cy="4" r="3" fill="none" stroke="#555" stroke-width="1"/><path d="M6.3 6.3 9 9" stroke="#555" stroke-width="1"/></svg>
  <svg class="icon" style="left:229px;top:17px" viewBox="0 0 10 10"><rect x="1.5" y="3" width="7" height="6" fill="none" stroke="#555" stroke-width=".9"/><path d="M3.5 3V2a1.5 1.5 0 0 1 3 0v1" fill="none" stroke="#555" stroke-width=".9"/></svg>

  <p class="crumb abs" style="left:18px;top:33px">Home / BILINGUAL BOOKS-HOME /<br><b>The Paper Moon - La Lune en Papier (English/French)</b></p>

  <div class="gallery">
    <div class="img" role="img" aria-label="Buchcover The Paper Moon – La Lune en Papier" style="left:23px;top:10px;width:67px;height:87px;background:linear-gradient(180deg,#e7c24c 0%,#9cc06a 45%,#5e8f43 100%);box-shadow:1px 1px 2px rgba(0,0,0,.25)"></div>
    <div class="img" role="img" aria-label="Innenseite: Wiese unter hellem Himmel" style="left:23px;top:102px;width:67px;height:67px;background:linear-gradient(180deg,#cfe3f1 0%,#b9d48a 60%,#7fa653 100%)"></div>
    <div class="img" role="img" aria-label="Ausmalseite" style="left:23px;top:172px;width:33px;height:33px;background:#f6f6f4"></div>
    <div class="img" role="img" aria-label="Ausmalseite mit Landschaft" style="left:57px;top:172px;width:33px;height:33px;background:#f1f1ee"></div>
    <div class="img" role="img" aria-label="Innenseite: Himmel über einem Feld" style="left:23px;top:209px;width:67px;height:68px;background:linear-gradient(180deg,#d8eaf4 0%,#cbd68e 60%,#b9a44e 100%)"></div>
  </div>

  <div class="info" style="top:49px">
    <p class="info__author">TAREK VOSS</p>
    <h1 class="info__title" style="margin-top:2px">The Paper Moon - La Lune en Papier (English/French)</h1>
    <p class="info__price" style="margin-top:3px">$12.95</p>
    <p class="info__small">Inkl. MwSt. und Versand</p>
    <div class="qty" style="margin-top:4px">Anzahl <span>-&nbsp;&nbsp;1&nbsp;&nbsp;+</span></div>
  </div>
  <div class="info" style="top:103px"><div class="btn btn--line" style="top:0">E-BOOK</div><div class="btn btn--solid" style="top:12px">PAPERBACK</div></div>

  <div class="info desc" style="top:130px">
    <p>A gentle story about home, courage and the people we love most.<br>"High above the village hung a little paper moon. She felt lonely and wished she could drift away and see the world from far above."</p>
    <p>When a kind night wind lifts her from her string, she floats over forests, rivers and towns. What will she find, what will she see? And will she find her way back to the window where she belongs?</p>
    <p>Kids will learn different places, objects, and simple questions and answers.</p>
    <p>Here's what makes this book special:</p>
    <p>Each sentence is both in English and French<br>The story is simple and suitable for early age learning<br>All the illustrations are original, creative, and fun<br>EXTRA PAGES for coloring</p>
    <p>Kids learn quickly and easily. With bilingual children's books, you set them up for success and widen their horizons from an early age! This dual language book is part of a series of bedtime stories that are made to teach children new foreign words and phrases as you read to them.</p>
    <p>Teach your children first words in English or French.</p>
  </div>

  <dl class="info specs" style="top:257px">
    <dt>Buchtitel</dt><dd>The Paper Moon - La Lune en Papier (English/French)</dd>
    <dt>Dateigröße</dt><dd>60 pages</dd>
    <dt>Autor</dt><dd>Tarek Voss</dd>
    <dt>ISBN</dt><dd>979-8750000000</dd>
    <dt>Edition Sprache</dt><dd>English, French</dd>
    <dt>Buchformat</dt><dd>8.5 x 11</dd>
    <dt>Veröffentlichungsdatum</dt><dd>October 29, 2021</dd>
  </dl>

  <h2 class="related__title">Related Products</h2>
  <div class="related__tile" style="left:17px"><div class="cover cover--moon" role="img" aria-label="Buchcover Der tanzende Mond"></div></div>
  <div class="related__tile" style="left:74px"><div class="cover cover--frog" role="img" aria-label="Buchcover Hüpf, kleiner Frosch"></div></div>
  <div class="related__tile" style="left:130px"><div class="cover cover--moon" role="img" aria-label="Buchcover Der tanzende Mond"></div></div>
  <div class="related__tile" style="left:186px"><div class="cover cover--frog" role="img" aria-label="Buchcover Hüpf, kleiner Frosch"></div></div>
  <p class="related__cap" style="left:17px">Der tanzende Mond<br>The Dancing Moon<br>$11.95</p>
  <p class="related__cap" style="left:74px">Hüpf, kleiner Frosch<br>Hop, Little Frog<br>$9.95</p>
  <p class="related__cap" style="left:130px">Der tanzende Mond<br>The Dancing Moon<br>$11.95</p>
  <p class="related__cap" style="left:186px">Hüpf, kleiner Frosch<br>Hop, Little Frog<br>$9.95</p>

  <footer class="foot">
    <div class="abs" style="left:19px;top:517px;width:90px"><h4>Kundenservice</h4><p style="margin-top:4px">Du hast Fragen zu unseren Büchern oder Deiner Bestellung?<br>Meld Dich einfach bei <b>hallo@sonnenfeldverlag.de</b> – wir antworten so schnell es geht.</p></div>
    <div class="abs" style="left:139px;top:517px"><h4>Kontakt</h4><ul style="margin-top:4px"><li>Handel</li><li>Presse</li><li>Karriere</li></ul></div>
    <div class="abs" style="left:193px;top:517px"><h4>Kleingedrucktes</h4><ul style="margin-top:4px"><li>Impressum</li><li>AGB</li><li>Datenschutzerklärung</li></ul></div>
    <div class="social" style="left:20px;top:561px"><span></span><span></span><span></span></div>
    <p class="copy abs" style="left:0;top:570px">© 2022, Sonnenfeld Verlag</p>
  </footer>
</section>

</body>
</html>
```